Online interactive calendar for training organisation

We have a new website being made and need a design for an online calendar that is interactive and very simple and easy to use. On our main page this calendar will include all of our courses (approx 30 different ones with up to 8 different locations). On our sub pages which have course information, the calendar will only include details of that specific course. Details needed are: Course code, course name/title, date, duration (1/2 day - 5 days), location, price, discount price. Maybe also a key for available or limited spots left? We want a section at the top of the calendar to be able to filter by location or course, and maybe to filter by month also? I have included a spreadsheet with a sample of our courses with this information. Also a sample draft of the main page on our new webpage to show the colour green which is our company colour. Main notes - we want as simple, effective and easy to use as possible.
We will need to know what plug in we can use to get the design you have created.

Target Market(s)

Mining and construction - both companies and individuals

Number of Pages Required

1 page

Colors
cadf82

Requirements
Must have
• Be simple, easy to use, effective.

```html
<!DOCTYPE html>
<html lang="en">
<head>
<meta charset="utf-8">
<title>Stonebridge Training – Online Calendar</title>
<link rel="stylesheet" href="https://fonts.googleapis.com/css2?family=Roboto:wght@300;400;500;700;900&display=swap">
<style>
  :root{
    --brand:#cadf82;
    --brand-dark:#a9c25a;
    --ink:#1c1c1c;
    --panel:#232323;
    --head:#151515;
    --row:#2b2b2b;
    --row-alt:#262626;
    --line:#3a3a3a;
    --field:#2f2f2f;
    --muted:#bdbdbd;
    --white:#ffffff;
    --body:#555555;
    --limited:#e8b23a;
    --full:#d9534f;
  }
  *{box-sizing:border-box;margin:0;padding:0}
  html,body{width:784px;height:1200px;overflow:hidden}
  body{font-family:"Roboto",Arial,sans-serif;background:var(--white);color:var(--body);position:relative}

  /* Hero */
  .hero{position:relative;height:241px;overflow:hidden}
  .hero-photo{position:absolute;inset:0;background:
      radial-gradient(ellipse at 20% 30%,#6b6b66 0%,transparent 55%),
      radial-gradient(ellipse at 85% 25%,#8a7a3a 0%,transparent 45%),
      linear-gradient(180deg,#4a4a48 0%,#2e2e2d 100%)}
  .hero-shade{position:absolute;inset:0;background:rgba(0,0,0,.38)}
  .site-nav{position:absolute;left:0;right:0;top:14px;height:26px;display:flex;align-items:center;padding:0 28px 0 58px}
  .brand{display:flex;align-items:center;gap:8px;color:var(--white);font-weight:900;font-size:15px;letter-spacing:.5px}
  .brand-mark{width:14px;height:14px;background:var(--white)}
  .nav-links{margin-left:auto;display:flex;gap:14px;list-style:none}
  .nav-links li{color:var(--white);font-size:8.5px;font-weight:500}
  .hero-copy{position:absolute;left:0;right:0;top:108px;text-align:center;color:var(--white)}
  .hero-title{font-size:22px;font-weight:900;letter-spacing:.3px;text-transform:uppercase}
  .hero-text{font-size:14px;font-weight:300;line-height:17px;margin:6px auto 0;width:440px}
  .btn{display:inline-block;font-size:7px;font-weight:700;text-transform:uppercase;letter-spacing:.5px;padding:6px 14px;border-radius:2px}
  .btn-brand{background:var(--brand);color:var(--ink)}
  .btn-dark{background:var(--ink);color:var(--white)}
  .hero .btn{margin-top:12px}

  /* Calendar */
  .calendar{background:var(--panel);height:592px;padding-top:96px;text-align:center}
  .calendar-title{color:var(--brand);font-size:24px;font-weight:900;text-transform:uppercase;letter-spacing:.5px}
  .calendar-tools{width:560px;margin:16px auto 0;display:flex;align-items:center;gap:8px}
  .filter{display:flex;align-items:center;justify-content:space-between;width:118px;height:20px;padding:0 7px;background:var(--field);border:1px solid var(--line);border-radius:2px;color:var(--muted);font-size:6.5px;text-align:left}
  .filter b{color:var(--white);font-weight:500;margin-right:4px}
  .filter svg{width:7px;height:7px;flex:none}
  .legend{margin-left:auto;display:flex;gap:10px;list-style:none;font-size:6.5px;color:var(--muted)}
  .legend li{display:flex;align-items:center;gap:4px}
  .dot{display:inline-block;width:6px;height:6px;border-radius:50%;background:var(--brand)}
  .dot.limited{background:var(--limited)}
  .dot.full{background:var(--full)}
  .course-table{margin:10px auto 0;width:560px;border-collapse:collapse;font-size:6px;text-align:left}
  .course-table th{background:var(--head);color:var(--white);font-weight:700;text-transform:uppercase;padding:0 6px;height:18px;white-space:nowrap}
  .course-table td{color:var(--muted);padding:0 6px;height:19px;border-bottom:1px solid var(--line);white-space:nowrap}
  .course-table tbody tr:nth-child(odd) td{background:var(--row)}
  .course-table tbody tr:nth-child(even) td{background:var(--row-alt)}
  .course-table td.course-name,.course-table td.discount{color:var(--brand);font-weight:500}
  .calendar .btn{margin-top:20px}

  /* Service */
  .service{position:relative;height:189px}
  .service-art{position:absolute;left:48px;top:12px;width:276px;height:166px;background:linear-gradient(135deg,#e9e6df 0%,#c9c3b6 45%,#8f8a80 100%);clip-path:polygon(10% 40%,55% 8%,98% 30%,96% 80%,50% 100%,6% 80%)}
  .service-copy{position:absolute;left:446px;top:40px;width:290px}
  .service-title{font-size:17px;font-weight:900;line-height:19px;text-transform:uppercase;color:var(--ink)}
  .service-title .accent{color:var(--brand-dark)}
  .service-text{font-size:6.5px;line-height:9px;margin:8px 0 12px;color:#777}

  /* Footer */
  .site-footer{background:var(--brand);height:178px;position:relative;color:var(--ink)}
  .footer-cols{position:absolute;top:22px;left:150px;right:60px;display:flex;gap:34px}
  .footer-about{width:150px}
  .footer-about .brand{color:var(--ink);font-size:14px;margin-bottom:10px}
  .footer-about .brand-mark{background:var(--ink)}
  .footer-col p{font-size:6px;line-height:8.5px}
  .footer-col h4{font-size:8px;font-weight:700;margin-bottom:8px}
  .footer-list{list-style:none;font-size:6px;line-height:11px}
  .footer-list li::before{content:"› ";}
  .footer-links{width:70px}
  .footer-contact{width:130px}
  .socials{display:flex;gap:6px;margin-top:10px}
  .socials span{width:14px;height:14px;border-radius:50%;background:var(--ink)}
  .copyright{position:absolute;left:150px;bottom:14px;font-size:6px}
</style>
</head>
<body>
  <header class="hero">
    <div class="hero-photo" role="img" aria-label="Builder's desk with plans, hard hat, safety glasses and tools"></div>
    <div class="hero-shade"></div>
    <nav class="site-nav">
      <div class="brand"><span class="brand-mark"></span>STONEBRIDGE</div>
      <ul class="nav-links">
        <li>Home</li><li>About</li><li>Services</li><li>Project</li><li>Blog</li><li>Contact</li>
      </ul>
    </nav>
    <div class="hero-copy">
      <h1 class="hero-title">We construct your dream in live</h1>
      <p class="hero-text">Lorem Ipsum is simply dummy text of the printing and typesetting industry. Lorem Ipsum has been the industry's</p>
      <span class="btn btn-brand">Read more</span>
    </div>
  </header>

  <section class="calendar">
    <h2 class="calendar-title">Online Calendar</h2>
    <div class="calendar-tools">
      <span class="filter"><span><b>Location</b>All locations</span><svg viewBox="0 0 8 8"><path d="M1 2.5 4 5.5 7 2.5" fill="none" stroke="#cadf82" stroke-width="1.4"/></svg></span>
      <span class="filter"><span><b>Course</b>All courses</span><svg viewBox="0 0 8 8"><path d="M1 2.5 4 5.5 7 2.5" fill="none" stroke="#cadf82" stroke-width="1.4"/></svg></span>
      <span class="filter"><span><b>Month</b>All months</span><svg viewBox="0 0 8 8"><path d="M1 2.5 4 5.5 7 2.5" fill="none" stroke="#cadf82" stroke-width="1.4"/></svg></span>
      <ul class="legend">
        <li><span class="dot"></span>Available</li>
        <li><span class="dot limited"></span>Limited spots</li>
        <li><span class="dot full"></span>Full</li>
      </ul>
    </div>
    <table class="course-table">
      <thead>
        <tr><th>Course Code &amp; Title</th><th>Course Date</th><th>Time</th><th>Price</th><th>Duration</th><th>Location</th><th>Discount Price</th><th>Spots</th></tr>
      </thead>
      <tbody>
        <tr><td class="course-name">CW101 Work Safely in Construction</td><td>Monday, October 20, 2014</td><td>8:00am</td><td>$450</td><td>1 Day</td><td>Brisbane</td><td class="discount">$390</td><td><span class="dot"></span></td></tr>
        <tr><td class="course-name">RII201 Operate Skid Steer Loader</td><td>Tuesday, October 21, 2014</td><td>8:00am</td><td>$780</td><td>2 Days</td><td>Mackay</td><td class="discount">$690</td><td><span class="dot limited"></span></td></tr>
        <tr><td class="course-name">WH301 Work at Heights</td><td>Monday, November 3, 2014</td><td>7:30am</td><td>$320</td><td>1/2 Day</td><td>Townsville</td><td class="discount">$280</td><td><span class="dot"></span></td></tr>
        <tr><td class="course-name">CS401 Confined Space Entry and Rescue</td><td>Friday, November 7, 2014</td><td>8:00am</td><td>$540</td><td>1 Day</td><td>Emerald</td><td class="discount">$480</td><td><span class="dot full"></span></td></tr>
        <tr><td class="course-name">FA102 Provide First Aid</td><td>By appointment</td><td>—</td><td>$160</td><td>1 Day</td><td>Brisbane</td><td class="discount">$140</td><td><span class="dot"></span></td></tr>
        <tr><td class="course-name">EX220 Excavator Operations</td><td>Tuesday, November 11, 2014</td><td>7:00am</td><td>$1,450</td><td>5 Days</td><td>Gladstone</td><td class="discount">$1,290</td><td><span class="dot limited"></span></td></tr>
        <tr><td class="course-name">FL150 Forklift Licence</td><td>Monday, November 17, 2014</td><td>8:00am</td><td>$620</td><td>3 Days</td><td>Rockhampton</td><td class="discount">$560</td><td><span class="dot"></span></td></tr>
        <tr><td class="course-name">DG310 Dogging and Rigging Basics</td><td>Thursday, November 20, 2014</td><td>8:00am</td><td>$890</td><td>4 Days</td><td>Mackay</td><td class="discount">$790</td><td><span class="dot"></span></td></tr>
        <tr><td class="course-name">GI110 Mine Site Induction</td><td>By appointment</td><td>—</td><td>$240</td><td>1 Day</td><td>Moranbah</td><td class="discount">$210</td><td><span class="dot limited"></span></td></tr>
        <tr><td class="course-name">SR205 Gas Test Atmospheres</td><td>Monday, December 1, 2014</td><td>8:00am</td><td>$380</td><td>1 Day</td><td>Emerald</td><td class="discount">$340</td><td><span class="dot"></span></td></tr>
        <tr><td class="course-name">TC120 Traffic Control</td><td>Friday, December 5, 2014</td><td>7:30am</td><td>$420</td><td>2 Days</td><td>Townsville</td><td class="discount">$370</td><td><span class="dot full"></span></td></tr>
        <tr><td class="course-name">PM330 Plant Maintenance</td><td>Wednesday, December 10, 2014</td><td>8:00am</td><td>$960</td><td>3 Days</td><td>Gladstone</td><td class="discount">$860</td><td><span class="dot"></span></td></tr>
      </tbody>
    </table>
    <span class="btn btn-brand">Load more</span>
  </section>

  <section class="service">
    <div class="service-art" role="img" aria-label="Illustration of a house under construction with timber frame and scaffolding"></div>
    <div class="service-copy">
      <h2 class="service-title"><span class="accent">Provide</span> the best quality service and <span class="accent">construct</span></h2>
      <p class="service-text">Lorem Ipsum is simply dummy text of the printing and typesetting industry. Lorem Ipsum has been the industry's standard dummy text ever since the 1500s, when an unknown printer took a galley of type and scrambled it to make a type specimen book. It has survived not only five centuries.</p>
      <span class="btn btn-dark">Read more</span>
    </div>
  </section>

  <footer class="site-footer">
    <div class="footer-cols">
      <div class="footer-col footer-about">
        <div class="brand"><span class="brand-mark"></span>STONEBRIDGE</div>
        <p>Lorem Ipsum is simply dummy text of the printing and typesetting industry. Lorem Ipsum has been the industry's standard dummy text ever since the 1500s, when an unknown printer took a galley of type and scrambled it to make a type specimen book.</p>
      </div>
      <div class="footer-col footer-links">
        <h4>Information</h4>
        <ul class="footer-list"><li>Home</li><li>About Us</li><li>Our Services</li><li>Our Project</li><li>Calendar</li><li>Blog</li></ul>
      </div>
      <div class="footer-col footer-links">
        <h4>Support</h4>
        <ul class="footer-list"><li>Help Desk</li><li>Contact</li><li>Terms of Use</li><li>Booking</li><li>Locations</li><li>Privacy Policy</li></ul>
      </div>
      <div class="footer-col footer-contact">
        <h4>Contact us</h4>
        <p>Lorem ipsum is simply dummy text of the printing and typesetting.<br><br>Address: 14 Quarry Rd, Stonefield 4000<br>Phone Number: 07 5550 1234<br>Email: info@stonebridge.test</p>
        <div class="socials"><span></span><span></span><span></span><span></span></div>
      </div>
    </div>
    <p class="copyright">Copyright © 2014 Stonebridge. All rights reserved.</p>
  </footer>
</body>
</html>
```